Biz Card & Stationary for Kids Indoor Play Space Company
Bramble Hollow
Biz Card & Stationary for Kids Indoor Play Space Company - Childcare
Creative Brief
Bright & Fun-filled
Marla Quint
Owner
7148 Garnet Ave. Ashbury Falls, OH 44712
marla.quint@bramblehollowplay.com
https://bramblehollowplay.com/
Would like the feel of the design to be consistent with our website. I will upload our logo. I will provide you with a biz phone # in a few days. If needed, our Logo Font is "Brady Bunch Remastered".
zestlark zestlark
1. In addition to biz cards design, we also want stationary design (letterhead and envelope). 2. We would like to see versions where our logo has a different tag line of "Indoor Play Center". Maybe this tag-line could be used on the front of the card and the original tag-line on the back of the card?

```html
<!DOCTYPE html>
<html lang="en">
<head>
<meta charset="utf-8">
<title>Bramble Hollow – Business Card</title>
<link href="https://fonts.googleapis.com/css2?family=Nunito:wght@400;600;700;800&display=swap" rel="stylesheet">
<style>
  :root {
    --bg: #2b2b2b;
    --card: #ffffff;
    --brand-blue: #1f5fae;
    --brand-red: #e4252f;
    --edge-blue: #2a6fc4;
    --text-grey: #4a4a4a;
    --photo-warm: #e8c9a0;
    --photo-mid: #c9a27a;
    --photo-cool: #a9c4d8;
  }
  * { box-sizing: border-box; margin: 0; padding: 0; }
  html, body { width: 1200px; height: 961px; overflow: hidden; }
  body {
    background: var(--bg);
    font-family: "Nunito", sans-serif;
    display: flex;
    flex-direction: column;
    align-items: center;
    justify-content: center;
    gap: 40px;
  }
  .card {
    width: 760px;
    height: 434px;
    background: var(--card);
    position: relative;
    overflow: hidden;
    border-bottom: 6px solid var(--edge-blue);
    box-shadow: 0 10px 30px rgba(0,0,0,.45);
  }
  /* Front: name side */
  .card-front {
    display: flex;
    align-items: center;
    justify-content: center;
  }
  .brand {
    display: flex;
    align-items: center;
    gap: 18px;
  }
  .brand-dot {
    width: 34px;
    height: 34px;
    border-radius: 50%;
    background: var(--brand-red);
  }
  .brand-name {
    font-family: "Nunito", sans-serif;
    font-weight: 800;
    font-size: 68px;
    color: var(--brand-blue);
    line-height: 1;
  }
  .front-url {
    position: absolute;
    right: 36px;
    bottom: 26px;
    font-size: 16px;
    font-weight: 700;
    color: var(--brand-red);
  }
  /* Back: photo + contact side */
  .photo-area {
    position: absolute;
    inset: 0;
    background: linear-gradient(120deg, var(--photo-cool) 0%, var(--photo-warm) 45%, var(--photo-mid) 100%);
  }
  .contact-fade {
    position: absolute;
    top: 0; right: 0; bottom: 0;
    width: 320px;
    background: linear-gradient(90deg, rgba(255,255,255,0) 0%, rgba(255,255,255,.92) 45%);
  }
  .cloud-band { position: absolute; left: 0; bottom: 0; }
  .contact-list {
    position: absolute;
    right: 30px;
    top: 120px;
    list-style: none;
    font-size: 16px;
    color: var(--text-grey);
  }
  .contact-list li {
    display: flex;
    justify-content: flex-end;
    align-items: center;
    gap: 10px;
    height: 26px;
  }
  .contact-list .spacer { height: 24px; }
  .contact-list svg { width: 16px; height: 16px; fill: var(--edge-blue); flex: none; }
  .person {
    position: absolute;
    left: 36px;
    bottom: 26px;
  }
  .person-name {
    font-weight: 700;
    font-size: 28px;
    line-height: 1.2;
    color: var(--brand-blue);
  }
  .person-role {
    font-size: 18px;
    color: var(--brand-red);
    font-weight: 600;
  }
  .person-address {
    font-size: 17px;
    color: var(--text-grey);
    margin-top: 6px;
  }
</style>
</head>
<body>
  <section class="card card-front">
    <div class="brand">
      <span class="brand-dot"></span>
      <span class="brand-name">Bramble Hollow</span>
    </div>
    <div class="front-url">bramblehollowplay.com</div>
  </section>

  <section class="card card-back">
    <div class="photo-area" role="img" aria-label="Photo of children playing with colourful toys in an indoor play room"></div>
    <div class="contact-fade"></div>
    <svg class="cloud-band" width="760" height="170" viewBox="0 0 760 170">
      <path d="M0,60 Q45,10 100,42 Q145,2 205,38 Q250,8 305,40 Q355,10 410,42 Q455,14 510,42 Q560,12 615,40 Q665,10 715,38 Q745,26 760,32 L760,170 L0,170 Z" fill="#ffffff"/>
    </svg>
    <ul class="contact-list">
      <li>555-214-3081
        <svg viewBox="0 0 24 24"><path d="M6.6 10.8a15 15 0 0 0 6.6 6.6l2.2-2.2c.3-.3.7-.4 1-.2 1.1.4 2.3.6 3.6.6.6 0 1 .4 1 1V20c0 .6-.4 1-1 1A17 17 0 0 1 3 4c0-.6.4-1 1-1h3.5c.6 0 1 .4 1 1 0 1.3.2 2.5.6 3.6.1.3 0 .7-.2 1z"/></svg>
      </li>
      <li>555-214-7730
        <svg viewBox="0 0 24 24"><rect x="7" y="2" width="10" height="20" rx="2"/></svg>
      </li>
      <li class="spacer"></li>
      <li>marla.quint@bramblehollowplay.com
        <svg viewBox="0 0 24 24"><path d="M2 5h20v14H2z M2 5l10 8 10-8" stroke="#fff" stroke-width="1.5"/></svg>
      </li>
      <li>www.bramblehollowplay.com
        <svg viewBox="0 0 24 24"><circle cx="12" cy="12" r="10"/><path d="M2 12h20M12 2c3 3 3 17 0 20M12 2c-3 3-3 17 0 20" stroke="#fff" stroke-width="1.3" fill="none"/></svg>
      </li>
    </ul>
    <div class="person">
      <div class="person-name">Marla Quint</div>
      <div class="person-role">Owner</div>
      <div class="person-address">7148 Garnet Ave. Ashbury Falls, OH 44712</div>
    </div>
  </section>
</body>
</html>
```